Tranquil Pathway Business Card

Logo attached. (will be printing onto thick white/off white textured card)

Double sided business card for two Therapists working at Tranquil Pathway.

Require one design, but with different name and mobile numbers on each card.

Target Market(s)

Medical, Health

Industry/Entity Type

Business

Contact Information for Business Card

Need one business card design, but a separate card for each person - Colin Marchetti and Marieke de Boeckx.

FRONT OF CARD

Logo

Name (Colin Marchetti on one card, Marieke de Boeckx on the other)
Professional Clinical Hypnotherapist

Consulting Rooms (Near Lindqvist Hospital)
482 Brackenfield Road
Dunmore VIC 3987

Colin@TranquilPathway.example.au OR Marieke@TranquilPathway.example.au

Mobile: 0455 872 604 (for Colin) OR
Mobile: 0467 290 518 (for Marieke)

BACK OF CARD

Logo

Website: www.TranquilPathway.example.au

Phone: 1300 958 471

Requirements
Must have
• Text and logo only. No additiional graphics.

```html
<!DOCTYPE html>
<html lang="en">
<head>
<meta charset="utf-8">
<title>Tranquil Pathway Business Card</title>
<link rel="stylesheet" href="https://fonts.googleapis.com/css2?family=Open+Sans:wght@400;600;700&display=swap">
<style>
  :root {
    --stage: #141414;
    --card-light: #f3f3f3;
    --navy: #1f2a64;
    --navy-deep: #1a2458;
    --ink: #111111;
    --white: #ffffff;
    --ring-faint: rgba(255, 255, 255, 0.06);
  }
  html, body {
    margin: 0;
    padding: 0;
    width: 1200px;
    height: 900px;
    overflow: hidden;
    background: var(--stage);
    font-family: "Open Sans", Arial, sans-serif;
  }
  .stage {
    position: relative;
    width: 1200px;
    height: 900px;
  }
  .card {
    position: absolute;
    top: 184px;
    width: 302px;
    height: 490px;
    border-radius: 12px;
    overflow: hidden;
    text-align: center;
  }
  .card--front {
    left: 299px;
    background: var(--card-light);
    color: var(--ink);
  }
  .card--back {
    left: 646px;
    background: var(--navy);
    color: var(--white);
  }
  .brand-mark {
    position: absolute;
    left: 101px;
    top: 34px;
    width: 100px;
    height: 100px;
    border-radius: 50%;
    background: var(--navy);
  }
  .brand-name {
    position: absolute;
    left: 0;
    right: 0;
    font-weight: 700;
    margin: 0;
    white-space: nowrap;
  }
  .card--front .brand-name {
    top: 150px;
    font-size: 27px;
    color: var(--navy);
  }
  .card--back .brand-name {
    top: 318px;
    font-size: 33px;
    color: var(--white);
  }
  .person {
    position: absolute;
    top: 271px;
    left: 0;
    right: 0;
  }
  .person-name {
    margin: 0;
    font-size: 17px;
    font-weight: 600;
    color: var(--navy);
    line-height: 22px;
  }
  .person-role {
    margin: 0;
    font-size: 13px;
    line-height: 18px;
  }
  .address {
    position: absolute;
    top: 347px;
    left: 0;
    right: 0;
    margin: 0;
    font-size: 13px;
    line-height: 21px;
    font-style: normal;
  }
  .contact {
    position: absolute;
    left: 0;
    right: 0;
    margin: 0;
    padding: 0;
    list-style: none;
    font-size: 13px;
    line-height: 21px;
  }
  .card--front .contact { top: 415px; }
  .card--back .contact { top: 411px; font-size: 14px; line-height: 26px; }
  .contact svg {
    width: 10px;
    height: 10px;
    margin-right: 3px;
    vertical-align: -1px;
  }
  .back-ring {
    position: absolute;
    left: 0;
    top: 0;
  }
</style>
</head>
<body>
<main class="stage">
  <section class="card card--front" aria-label="Business card front">
    <div class="brand-mark" aria-hidden="true"></div>
    <p class="brand-name">Tranquil Pathway</p>
    <div class="person">
      <p class="person-name">Colin Marchetti</p>
      <p class="person-role">Professional Clinical Hypnotherapist</p>
    </div>
    <address class="address">Consulting Rooms&nbsp; 482<br>Brackenfield Road Dunmore VIC 3987</address>
    <ul class="contact">
      <li><svg viewBox="0 0 10 10" aria-hidden="true"><rect x="2.5" y="0.5" width="5" height="9" rx="1" fill="none" stroke="#1f2a64" stroke-width="1.2"/></svg>0455 872 604</li>
      <li><svg viewBox="0 0 10 10" aria-hidden="true"><rect x="0" y="1.5" width="10" height="7" fill="#1f2a64"/><path d="M0 1.5 L5 5.5 L10 1.5" fill="none" stroke="#f3f3f3" stroke-width="0.8"/></svg>Colin@TranquilPathway.example.au</li>
    </ul>
  </section>

  <section class="card card--back" aria-label="Business card back">
    <svg class="back-ring" width="302" height="490" viewBox="0 0 302 490" aria-hidden="true">
      <circle cx="151" cy="176" r="160" fill="none" stroke="var(--ring-faint)" stroke-width="26"/>
    </svg>
    <p class="brand-name">Tranquil Pathway</p>
    <ul class="contact">
      <li><svg viewBox="0 0 10 10" aria-hidden="true"><circle cx="5" cy="5" r="4.5" fill="#ffffff"/><path d="M0.5 5 H9.5 M5 0.5 V9.5" stroke="#1f2a64" stroke-width="0.8"/></svg>www.TranquilPathway.example.au</li>
      <li><svg viewBox="0 0 10 10" aria-hidden="true"><path d="M2 0.5 L4 2.8 L3 4 Q4.5 6 6 7 L7.2 6 L9.5 8 L8.2 9.5 Q4 9 0.5 2 Z" fill="#ffffff"/></svg>1300 958 471</li>
    </ul>
  </section>
</main>
</body>
</html>
```